Redesign Current Website Into An Exciting Updated Design

We need to redesign the current website www.glintvaultoffers.net We want an overall new look. We are rebranding so it will be a new logo and we would like to see new images as well so you cannot compare the old from the new.

You can use same exact content as on current url www.glintvaultoffers.net

The website must be warm and inviting and fun yet professional and modern.

The website must also be designed with mobile in mind

The website must be warm and inviting yet professional and modern.

The website must also be designed with mobile in mind.

Target Market(s)

Consumers redeeming rewards

Industry/Entity Type

Promotional Reward Fullfillment

Coding

Coded - Design and coding required

Number of Pages Required

3 page

Requirements
Must have
• This website is a website where consumers come to redeem rewards they received from doing business with a company that offers these rewards. So the website should be very inviting.
Nice to have
• open
Should not have
• open

```html
<!DOCTYPE html>
<html lang="en">
<head>
<meta charset="utf-8">
<title>Kindly Rewards – Online Redemption System</title>
<link rel="stylesheet" href="https://fonts.googleapis.com/css2?family=Bebas+Neue&family=Poppins:wght@400;500;600&display=swap">
<style>
:root{
  --navy:#1f4f82;
  --navy-dark:#173f6a;
  --blue:#2a6aa8;
  --sky:#eef5fc;
  --ink:#333a44;
  --white:#fff;
  --gold:#f3b321;
}
*{box-sizing:border-box;margin:0;padding:0}
html,body{width:1200px;height:4640px;overflow:hidden}
body{position:relative;font-family:'Poppins',sans-serif;color:var(--ink);background:var(--white)}
.abs{position:absolute}
.display{font-family:'Bebas Neue',sans-serif;font-weight:400;line-height:.95}

/* brand name */
.brand-name{display:flex;align-items:center;gap:8px;font-family:'Poppins',sans-serif;font-weight:600;color:var(--navy);white-space:nowrap}
.brand-name i{display:block;background:var(--navy)}
.brand-name.light{color:#fff}
.brand-name.light i{background:#fff}

/* header */
.site-header{position:absolute;top:0;left:0;width:1200px;height:110px;background:var(--white);z-index:3}
.brand-box{position:absolute;left:44px;top:0;width:202px;height:157px;background:var(--white);display:flex;align-items:center;justify-content:center;z-index:4}
.brand-box .brand-name{font-size:18px}
.brand-box .brand-name i{width:12px;height:12px}
.nav a{position:absolute;top:54px;font-size:13px;color:#222;text-decoration:none}
.nav a.active{color:var(--blue);border-bottom:2px solid var(--blue);padding-bottom:9px}
.btn-contact{position:absolute;left:1004px;top:41px;width:129px;height:40px;background:var(--navy);color:#fff;font-size:12px;font-weight:600;display:flex;align-items:center;justify-content:center}

/* hero */
.hero{position:absolute;top:110px;left:0;width:1200px;height:752px}
.hero-photo{position:absolute;inset:0;background:linear-gradient(110deg,#0b4d6e 0%,#127a94 35%,#1fb5c0 60%,#2a6a4a 85%,#1d4b30 100%)}
.hero-panel{position:absolute;left:70px;top:75px;width:535px;height:677px;background:rgba(18,60,100,.55)}
.hero-welcome{position:absolute;left:138px;top:135px;font-size:42px;color:#fff}
.hero-title{position:absolute;left:138px;top:188px;font-size:104px;color:#fff;line-height:1}
.btn-outline{position:absolute;left:141px;top:525px;width:213px;height:57px;border:2px solid #fff;color:#fff;font-size:15px;font-weight:500;display:flex;align-items:center;justify-content:center;gap:16px}
.dots{position:absolute;left:571px;top:688px;display:flex;gap:6px}
.dots i{width:10px;height:10px;border-radius:50%;background:rgba(255,255,255,.5)}
.dots i:first-child{background:#fff}

/* section heading */
.heading{position:absolute;border-left:3px solid var(--navy);border-bottom:3px solid var(--navy);padding:22px 18px 10px 18px;color:var(--navy)}
.heading span{font-family:'Bebas Neue',sans-serif;display:block;line-height:.9}

/* about */
.about{position:absolute;top:862px;left:0;width:1200px;height:620px;background:var(--sky)}
.about-ring{position:absolute;left:87px;top:98px;width:430px;height:430px;border-radius:50%;border:3px solid var(--navy);background:#fff}
.about-photo{position:absolute;left:113px;top:124px;width:378px;height:378px;border-radius:50%;background:radial-gradient(circle at 50% 40%,#bfe3f5,#7ec3e6 60%,#8fb6c9)}
.about-text{position:absolute;left:581px;top:238px;width:553px;font-size:14px;line-height:26.7px;text-align:justify}
.btn-solid{position:absolute;background:var(--navy);color:#fff;font-weight:600;display:flex;align-items:center;justify-content:center;gap:14px}

/* services */
.services{position:absolute;top:1482px;left:0;width:1200px;height:1173px;background:#fff}
.hub-outer{position:absolute;left:378px;top:288px;width:450px;height:450px;border-radius:50%;background:#f1f7fd}
.hub-inner{position:absolute;left:440px;top:390px;width:320px;height:320px;border-radius:50%;background:#fff;box-shadow:0 6px 22px rgba(0,0,0,.15);display:flex;align-items:center;justify-content:center}
.hub-inner .brand-name{font-size:24px}
.hub-inner .brand-name i{width:16px;height:16px}
.service-card{position:absolute;width:294px;height:245px;border-radius:18px;overflow:hidden;box-shadow:0 4px 12px rgba(0,0,0,.15)}
.service-card .photo{position:absolute;inset:0}
.service-card .label{position:absolute;left:0;right:0;bottom:0;height:110px;background:linear-gradient(transparent,rgba(31,79,160,.95));color:#fff;font-weight:600;font-size:22px;line-height:27px;text-align:center;display:flex;align-items:flex-end;justify-content:center;padding-bottom:16px}

/* redeem */
.redeem{position:absolute;top:2655px;left:0;width:1200px;height:570px}
.redeem-photo{position:absolute;inset:0;background:linear-gradient(90deg,#1d5fa8 0%,#2a78b8 40%,#4fb7d0 65%,#7fd3d6 85%,#9ad7cf 100%)}
.redeem-copy{position:absolute;left:85px;top:240px;width:575px;font-size:13px;line-height:26.5px;color:#fff;text-align:justify}
.field{position:absolute;top:348px;height:59px;background:#fff;font-size:12px;font-weight:600;color:#222;display:flex;align-items:center;padding-left:18px}
.btn-go{position:absolute;left:85px;top:430px;width:209px;height:58px;background:var(--navy-dark);color:#fff;font-size:26px;font-weight:600;display:flex;align-items:center;justify-content:center;gap:42px}

/* testimonials */
.testimonials{position:absolute;top:3225px;left:0;width:1200px;height:770px;background:#fff}
.t-back{position:absolute;left:83px;top:335px;width:1032px;height:300px;border-radius:40px;background:var(--navy)}
.t-card{position:absolute;left:112px;top:300px;width:973px;height:360px;border-radius:40px;background:#f3f8fd;box-shadow:0 4px 18px rgba(0,0,0,.12)}
.t-ring{position:absolute;left:205px;top:345px;width:280px;height:270px;border-radius:50%;background:var(--navy)}
.t-photo{position:absolute;left:228px;top:350px;width:258px;height:258px;border-radius:50%;background:linear-gradient(160deg,#e6e9ee,#c9ced6)}
.t-name{position:absolute;left:537px;top:362px;font-size:26px;font-weight:600;color:var(--navy)}
.t-place{position:absolute;left:537px;top:400px;font-size:14px;font-weight:600;color:var(--navy)}
.t-stars{position:absolute;left:537px;top:424px;display:flex;gap:3px}
.t-quote{position:absolute;left:540px;top:475px;width:455px;font-size:14px;line-height:27.5px;color:var(--blue)}
.arrow-btn{position:absolute;width:48px;height:48px;border-radius:50%;display:flex;align-items:center;justify-content:center}
.arrow-btn.light{background:#fff;border:2px solid var(--navy)}
.arrow-btn.dark{background:var(--navy)}

/* clients */
.clients{position:absolute;top:3995px;left:0;width:1200px;height:440px;background:var(--sky)}
.client-logo{position:absolute;top:243px;width:198px;height:82px;background:#fff;border:1px solid #d9e2ec;display:flex;align-items:center;justify-content:center;gap:8px;font-size:17px;font-weight:600;color:var(--navy)}
.client-logo i{width:12px;height:12px;background:var(--navy);border-radius:50%}

/* footer */
.site-footer{position:absolute;top:4435px;left:0;width:1200px;height:205px;background:var(--navy);color:#fff}
.foot-links{position:absolute;left:70px;font-size:13px}
.foot-line{position:absolute;top:140px;height:1px;background:rgba(255,255,255,.6)}
.foot-brand{position:absolute;left:500px;top:80px;width:200px;display:flex;justify-content:center}
.foot-brand .brand-name{font-size:18px}
.foot-brand .brand-name i{width:12px;height:12px}
.social{position:absolute;left:1016px;top:62px;display:flex;gap:7px}
.social i{width:24px;height:24px;border-radius:50%;background:#fff}
.copy{position:absolute;top:170px;font-size:11px}
</style>
</head>
<body>

<header class="site-header">
  <div class="brand-box">
    <div class="brand-name"><i></i>Kindly Rewards</div>
  </div>
  <nav class="nav">
    <a class="active" style="left:326px">HOME</a>
    <a style="left:407px">ABOUT US</a>
    <a style="left:515px">SERVICES</a>
    <a style="left:620px">TESTIMONIALS</a>
    <a style="left:758px">ALREADY REDEEMED?</a>
    <a style="left:941px">HELP</a>
  </nav>
  <div class="btn-contact">CONTACT US</div>
</header>

<section class="hero">
  <div class="hero-photo" role="img" aria-label="Aerial view of a tropical island with overwater bungalows and turquoise sea"></div>
  <div class="hero-panel"></div>
  <div class="hero-welcome display">Welcome to</div>
  <h1 class="hero-title display">The Online<br>Redemption<br>System</h1>
  <div class="btn-outline">LEARN MORE
    <svg width="26" height="26" viewBox="0 0 26 26" fill="none" stroke="#fff" stroke-width="1.8"><path d="M13 2 24 13 13 24 2 13Z"/><path d="M7 13h12M14 8l5 5-5 5"/></svg>
  </div>
  <div class="dots"><i></i><i></i><i></i><i></i></div>
</section>

<section class="about">
  <div class="about-ring"></div>
  <div class="about-photo" role="img" aria-label="Traveller sitting on a suitcase surrounded by world landmarks"></div>
  <div class="heading" style="left:582px;top:80px"><span style="font-size:64px">About Us</span></div>
  <p class="about-text">We provide marketing incentives in the form of gift certificates and vouchers that are redeemable for a variety of items such as: discount travel, smart device products, restaurant incentives , golf discounts and more to thousands of businesses around the world who use them to create exciting marketing promotions and giveaways, customer loyalty programs, promotional contests and use them as customer appreciation gifts.</p>
  <div class="btn-solid" style="left:581px;top:438px;width:322px;height:60px;font-size:16px">REDEEM YOUR OFFER NOW
    <svg width="26" height="26" viewBox="0 0 26 26" fill="none" stroke="#fff" stroke-width="1.8"><path d="M13 2 24 13 13 24 2 13Z"/><path d="M7 13h12M14 8l5 5-5 5"/></svg>
  </div>
</section>

<section class="services">
  <div class="heading" style="left:428px;top:75px"><span style="font-size:72px">Our Services</span></div>
  <div class="hub-outer"></div>
  <div class="hub-inner"><div class="brand-name"><i></i>Kindly Rewards</div></div>
  <div class="service-card" style="left:70px;top:303px">
    <div class="photo" role="img" aria-label="Grocery store produce aisles" style="background:linear-gradient(160deg,#c79a55,#8a6a3a 50%,#5c7d3a)"></div>
    <div class="label">Gas &amp; Grocery<br>Rewards</div>
  </div>
  <div class="service-card" style="left:838px;top:303px">
    <div class="photo" role="img" aria-label="Tropical island mountain with overwater bungalows" style="background:linear-gradient(180deg,#6fb3e3,#3f7a5a 50%,#2fb7c6)"></div>
    <div class="label">Vacation Certificates</div>
  </div>
  <div class="service-card" style="left:68px;top:621px">
    <div class="photo" role="img" aria-label="Cosy restaurant interior with hanging lights" style="background:linear-gradient(160deg,#6e5a46,#a6876a 50%,#3e4c58)"></div>
    <div class="label">Dining Incentives</div>
  </div>
  <div class="service-card" style="left:840px;top:621px">
    <div class="photo" role="img" aria-label="Passenger airliner flying above clouds" style="background:linear-gradient(180deg,#3c7fd0,#7db4ea 55%,#dbe9f7)"></div>
    <div class="label">Travel Vouchers</div>
  </div>
  <div class="service-card" style="left:453px;top:818px">
    <div class="photo" role="img" aria-label="Hand holding a smartphone on a smart home device" style="background:linear-gradient(160deg,#e9e6e2,#bfb9b3 55%,#3a3a40)"></div>
    <div class="label">Digital<br>Electronic Products</div>
  </div>
</section>

<section class="redeem">
  <div class="redeem-photo" role="img" aria-label="Thatched hut over clear tropical water with palm trees"></div>
  <div class="heading" style="left:85px;top:72px;border-color:#fff;color:#fff"><span style="font-size:74px">Redeem Your Offer</span></div>
  <p class="redeem-copy">To Learn More About Your Offer Including The Full Details, How It Works, Terms, FAQ's and To Redeem and Activate Your Certificate Please Enter A Valid Certificate Number and Email.</p>
  <div class="field" style="left:85px;width:297px">CERTIFICATE ID</div>
  <div class="field" style="left:390px;width:296px">ENTER EMAIL ADDRESS</div>
  <div class="btn-go">GO
    <svg width="38" height="38" viewBox="0 0 26 26" fill="none" stroke="#fff" stroke-width="1.5"><path d="M13 2 24 13 13 24 2 13Z"/><path d="M7 13h12M14 8l5 5-5 5"/></svg>
  </div>
</section>

<section class="testimonials">
  <div class="heading" style="left:373px;top:80px"><span style="font-size:72px">Our Testimonials</span></div>
  <div class="t-back"></div>
  <div class="t-card"></div>
  <div class="t-ring"></div>
  <div class="t-photo" role="img" aria-label="Portrait of a smiling customer"></div>
  <div class="t-name">MARISOL VANTRECK</div>
  <div class="t-place">RIVERSIDE, CA</div>
  <div class="t-stars">
    <svg width="104" height="20" viewBox="0 0 104 20" fill="var(--gold)">
      <path id="st" d="M10 1l2.6 6 6.4.5-4.9 4.2 1.5 6.3L10 14.6 4.4 18l1.5-6.3L1 7.5 7.4 7z"/>
      <use href="#st" x="21"/><use href="#st" x="42"/><use href="#st" x="63"/><use href="#st" x="84"/>
    </svg>
  </div>
  <svg class="abs" style="left:934px;top:370px" width="50" height="40" viewBox="0 0 50 40" fill="var(--navy)"><path d="M0 0h20v20l-8 20H4l6-18H0zM28 0h20v20l-8 20h-8l6-18H28z"/></svg>
  <p class="t-quote">"I just booked a vacation with them and Delia Norwood was my agent. She was very helpful and professional, was able to answer all my questions, and help me make the best decision for my up coming vacation. I'm really excited and look forward to working with her again!"</p>
  <div class="arrow-btn light" style="left:67px;top:456px"><svg width="14" height="14" viewBox="0 0 14 14" fill="none" stroke="var(--navy)" stroke-width="2.4"><path d="M9 2 4 7l5 5"/></svg></div>
  <div class="arrow-btn dark" style="left:1085px;top:456px"><svg width="14" height="14" viewBox="0 0 14 14" fill="none" stroke="#fff" stroke-width="2.4"><path d="M5 2l5 5-5 5"/></svg></div>
</section>

<section class="clients">
  <div class="heading" style="left:445px;top:55px"><span style="font-size:72px">Our Clients</span></div>
  <div class="arrow-btn light" style="left:67px;top:261px"><svg width="14" height="14" viewBox="0 0 14 14" fill="none" stroke="var(--navy)" stroke-width="2.4"><path d="M9 2 4 7l5 5"/></svg></div>
  <div class="client-logo" style="left:170px"><i></i>Orbitrail</div>
  <div class="client-logo" style="left:393px;font-size:15px">Coachline League</div>
  <div class="client-logo" style="left:612px">Meridian Homes</div>
  <div class="client-logo" style="left:830px"><i></i>Kestrel Motors</div>
  <div class="arrow-btn dark" style="left:1085px;top:261px"><svg width="14" height="14" viewBox="0 0 14 14" fill="none" stroke="#fff" stroke-width="2.4"><path d="M5 2l5 5-5 5"/></svg></div>
</section>

<footer class="site-footer">
  <div class="foot-links" style="top:68px">About Us &nbsp;| &nbsp;Services &nbsp;| &nbsp;Testimonials</div>
  <div class="foot-links" style="top:100px">About Us &nbsp;| &nbsp;Help &nbsp;| &nbsp;Contact US</div>
  <div class="foot-brand"><div class="brand-name light"><i></i>Kindly Rewards</div></div>
  <div class="social"><i></i><i></i><i></i><i></i></div>
  <div class="foot-line" style="left:70px;width:405px"></div>
  <div class="foot-line" style="left:728px;width:407px"></div>
  <div class="copy" style="left:70px">© Copyright 2005-2025. All Rights Reserved.</div>
  <div class="copy" style="left:950px">Privacy Policy &nbsp;&nbsp;| &nbsp;&nbsp;Terms Of Use</div>
</footer>

</body>
</html>
```